Stationary Design using supplied logo

24 Hour Completion required after acceptance

Business Cards
Letter Head
With Compliments Slips
Web Page Theme

Please only use a the following colors:

Red
Charcoal
Chrome/Silver
White

Red being the DOMINANT Color

Please email questions you may have.

Continued work available to suitably motivated designer.

```html
<!DOCTYPE html>
<html lang="en">
<head>
<meta charset="utf-8">
<title>Pine Ledger – With Compliments Slip</title>
<link rel="stylesheet" href="https://fonts.googleapis.com/css2?family=Urbanist:ital,wght@0,400;0,500;0,700;1,400&display=swap">
<style>
  :root {
    --red: #b01a24;
    --charcoal: #2e2c2e;
    --text: #3a3a3a;
    --paper: #ffffff;
    --backdrop: #5b5b5b;
  }
  * { margin: 0; padding: 0; box-sizing: border-box; }
  html, body {
    width: 1200px; height: 1000px; overflow: hidden;
    background: var(--backdrop);
    font-family: "Urbanist", "Century Gothic", sans-serif;
  }
  .slip {
    position: absolute; left: 235px; top: 322px;
    width: 736px; height: 351px;
    background: var(--paper);
  }
  .brand { position: absolute; left: 38px; top: 30px; }
  .brand-name {
    display: flex; align-items: center; gap: 8px;
    font-size: 46px; font-weight: 400; line-height: 1;
    color: var(--charcoal); letter-spacing: 0.5px;
  }
  .brand-dot {
    width: 20px; height: 20px; border-radius: 50%;
    background: var(--red); flex: none;
  }
  .brand-tagline {
    margin-top: 6px; margin-left: 2px;
    font-size: 10px; font-weight: 500; letter-spacing: 3.1px;
    color: var(--charcoal); text-transform: uppercase;
  }
  .slip-title {
    position: absolute; right: 35px; top: 56px;
    font-size: 29px; font-style: italic; font-weight: 400;
    color: var(--charcoal); letter-spacing: 0.3px;
  }
  .slip-title .accent { color: var(--red); }
  .offices {
    position: absolute; left: 38px; top: 270px;
    list-style: none; font-size: 10.5px; line-height: 15px; color: var(--text);
  }
  .offices .label { color: var(--red); font-weight: 700; }
  .contacts {
    position: absolute; top: 284px; left: 310px;
    display: flex; gap: 16px; font-size: 10.5px; line-height: 15px; color: var(--text);
  }
  .contact-col { list-style: none; }
  .contact-col li { display: flex; align-items: center; gap: 6px; }
  .contact-col svg { width: 10px; height: 10px; flex: none; }
  .contact-col.postal { margin-left: 14px; }
  .footer-band {
    position: absolute; left: 0; bottom: 0; width: 100%; height: 18px;
    display: flex; gap: 4px;
  }
  .footer-band .band-red { width: 286px; background: var(--red); }
  .footer-band .band-charcoal { flex: 1; background: var(--charcoal); }
</style>
</head>
<body>
  <section class="slip">
    <header class="brand">
      <div class="brand-name">pine ledger<span class="brand-dot"></span></div>
      <div class="brand-tagline">Members who matter</div>
    </header>

    <h1 class="slip-title"><span class="accent">WITH</span> COMPLIMENTS</h1>

    <ul class="offices">
      <li><span class="label">HEAD OFFICE:</span> Harlow St Ashfield</li>
      <li><span class="label">DUNMORE</span>: Cnr Reed St &amp; Marlow Cres Dunmore</li>
      <li><span class="label">WESTVALE</span>: Ellis Chambers Westvale</li>
    </ul>

    <div class="contacts">
      <ul class="contact-col">
        <li>
          <svg viewBox="0 0 10 10" aria-hidden="true"><circle cx="5" cy="5" r="4.4" fill="none" stroke="var(--red)" stroke-width="1"/><path d="M3.3 2.6c-.5.4-.3 1.8.9 3s2.5 1.5 3 .9l-.9-.9-.6.4C5 5.7 4.4 5 4.1 4.3l.4-.6z" fill="var(--red)"/></svg>
          02 5550 1000
        </li>
        <li>
          <svg viewBox="0 0 10 10" aria-hidden="true"><circle cx="5" cy="5" r="4.6" fill="var(--red)"/><rect x="2.5" y="4.2" width="5" height="2.8" fill="#fff"/><rect x="3.4" y="2.6" width="3.2" height="1.6" fill="#fff"/></svg>
          02 5550 1022
        </li>
      </ul>
      <ul class="contact-col">
        <li>
          <svg viewBox="0 0 10 10" aria-hidden="true"><circle cx="5" cy="5" r="4.6" fill="var(--red)"/><rect x="2.4" y="3.3" width="5.2" height="3.4" fill="#fff"/><path d="M2.4 3.3 5 5.3l2.6-2" fill="none" stroke="var(--red)" stroke-width=".7"/></svg>
          hello@pineledgeronline.com.au
        </li>
        <li>
          <svg viewBox="0 0 10 10" aria-hidden="true" fill="none" stroke="var(--red)" stroke-width=".9"><circle cx="5" cy="5" r="4.3"/><ellipse cx="5" cy="5" rx="1.8" ry="4.3"/><path d="M.7 5h8.6M1.5 3h7M1.5 7h7"/></svg>
          www.pineledgeronline.com.au
        </li>
      </ul>
      <ul class="contact-col postal">
        <li>PO Box 1200</li>
        <li>Ashfield DC 2999</li>
      </ul>
    </div>

    <div class="footer-band">
      <div class="band-red"></div>
      <div class="band-charcoal"></div>
    </div>
  </section>
</body>
</html>
```